Wine label design for my wife. Wine called "The Mirabel"

I need a wine label face lift of one of my premium wines in my collection. My wine sells in Harbor Lark's all over the States. My current label is called The Mirabel (my wife's name) and the illustration of her eyes is done by a well know artist from South Africa. I do not have to use this illustration and therefor I attached several pictures of her and her eyes, even when she was a little girl. The wine's also made in South Africa. This is a premium wine that we only sell 2000 bottles per year. The wine sells at 60 usd per bottle, The current label is too white. I also think her eyes should look more at the person buying it, than away from them.

Target Market(s)

Top end wine buyers

Font styles to use
Decorative
Script

Requirements
Must have
• 'The Mirabel' must be on the label
An illustration must be on the label
Basically all the info that's on the current label must be on by law. As per Sample
Nice to have
• Maybe some ideas of her whole face?
Should not have
• any gold colour

```html
<!DOCTYPE html>
<html lang="en">
<head>
<meta charset="UTF-8">
<title>The Mirabel – Sauvignon Blanc 2017 Label</title>
<link href="https://fonts.googleapis.com/css2?family=Abril+Fatface&family=Great+Vibes&family=Libre+Caslon+Text&family=Oswald:wght@600&display=swap" rel="stylesheet">
<style>
  :root {
    --backdrop: #15202c;
    --label-paper: #ddd6ca;
    --label-grain: #d0c8ba;
    --ink: #1e1e1e;
    --accent: #6b1f2f;
    --accent-light: #8e3447;
    --portrait-light: #c9c2b6;
    --portrait-dark: #5f5a54;
  }
  * { box-sizing: border-box; margin: 0; padding: 0; }
  html, body {
    width: 1200px;
    height: 948px;
    overflow: hidden;
    background: var(--backdrop);
  }
  .canvas {
    width: 1200px;
    height: 948px;
    display: flex;
    align-items: center;
    justify-content: center;
  }
  .wine-label {
    position: relative;
    width: 560px;
    height: 640px;
    background:
      repeating-linear-gradient(0deg, var(--label-paper) 0 3px, var(--label-grain) 3px 4px);
    color: var(--ink);
  }
  .wine-name {
    position: absolute;
    top: 40px;
    left: 0;
    right: 0;
    text-align: center;
  }
  .wine-name__monogram {
    display: block;
    height: 110px;
    font-family: "Great Vibes", cursive;
    font-size: 110px;
    line-height: 110px;
    color: var(--accent);
  }
  .wine-name__title {
    margin-top: 20px;
    font-family: "Abril Fatface", serif;
    font-weight: 400;
    font-size: 58px;
    letter-spacing: 1px;
    line-height: 1;
    text-transform: uppercase;
  }
  .varietal {
    position: absolute;
    top: 262px;
    left: 0;
    right: 0;
    text-align: center;
    font-family: "Libre Caslon Text", serif;
    font-size: 32px;
    line-height: 1;
    letter-spacing: 1px;
    text-transform: uppercase;
  }
  .portrait-band {
    position: absolute;
    top: 318px;
    left: 0;
    right: 0;
    height: 170px;
  }
  .portrait-band__rule {
    position: absolute;
    left: 0;
    right: 0;
    height: 6px;
    background: linear-gradient(90deg, var(--accent), var(--accent-light), var(--accent));
  }
  .portrait-band__rule--top { top: 0; }
  .portrait-band__rule--bottom { bottom: 0; }
  .portrait-band__art {
    position: absolute;
    top: 12px;
    bottom: 12px;
    left: 40px;
    right: 40px;
    background: linear-gradient(90deg, var(--portrait-light) 0%, #a9a298 45%, var(--portrait-dark) 100%);
  }
  .producer {
    position: absolute;
    bottom: 70px;
    left: 0;
    right: 0;
    text-align: center;
    font-family: "Oswald", sans-serif;
    font-weight: 600;
    font-size: 24px;
    line-height: 1;
    letter-spacing: 1px;
    text-transform: uppercase;
  }
</style>
</head>
<body>
  <main class="canvas">
    <article class="wine-label">
      <header class="wine-name">
        <span class="wine-name__monogram" aria-hidden="true">M</span>
        <h1 class="wine-name__title">The Mirabel</h1>
      </header>
      <p class="varietal">Sauvignon Blanc 2017</p>
      <section class="portrait-band">
        <div class="portrait-band__rule portrait-band__rule--top"></div>
        <div class="portrait-band__art" role="img" aria-label="Monochrome illustration of a woman's eyes across the band"></div>
        <div class="portrait-band__rule portrait-band__rule--bottom"></div>
      </section>
      <footer class="producer">Daniel Rowe Wines</footer>
    </article>
  </main>
</body>
</html>
```